Pruitt Denatl Laboratory nees a window design

We want to make a window cover 8 feet wide and 6 feet tall to advertise our dental lab with all the products we produce<br/>: Digital Cad/Cam<br/>: Implants<br/>: Dentures<br/>: Cast Partials <br/>: Orthodontic appliances<br/><br/> and it has to include a service we provide for a denturist on site by appointment only.<br/><br/>Please use the sample logo below our colours are white backround and blue letters

Font styles to use
Script

Colors
ffffff
0355a3

Requirements
Nice to have
• a picture of a teddy bear on a dental chair, or some dental work particularly bridge work since our moto is Building bridges since 1976
Should not have
• real people

```html
<!DOCTYPE html>
<html lang="en">
<head>
<meta charset="utf-8">
<title>Pruitt Denatl Laboratory – Window Cover</title>
<link rel="stylesheet" href="https://fonts.googleapis.com/css2?family=Crimson+Pro:ital,wght@0,800;1,600&display=swap">
<style>
  :root {
    --backdrop: #231f20;
    --brand-blue: #0355a3;
    --logo-blue: #1b88cc;
    --white: #ffffff;
    --sky: #d4e9f5;
    --chair-blue: #6bb8e6;
    --chair-grey: #d9dde0;
  }
  * { margin: 0; padding: 0; box-sizing: border-box; }
  html, body {
    width: 1200px; height: 1200px; overflow: hidden;
    background: var(--backdrop);
  }
  .canvas { position: relative; width: 1200px; height: 1200px; }
  .window-cover {
    position: absolute; left: 0; top: 300px;
    width: 1200px; height: 600px; overflow: hidden;
    background: radial-gradient(ellipse 60% 70% at 30% 50%, var(--white) 0%, #eef6fb 45%, var(--sky) 100%);
  }
  .top-band {
    position: absolute; left: 0; top: 0; width: 100%; height: 20px;
    background: var(--brand-blue);
  }
  .brand-mark {
    position: absolute; left: 60px; top: 110px;
    width: 84px; height: 84px; border-radius: 50%;
    background: var(--logo-blue);
  }
  .brand-name {
    position: absolute; left: 166px; top: 82px; width: 584px;
    font-family: "Crimson Pro", serif;
    font-weight: 800; font-size: 62px; line-height: 1.08;
    color: var(--logo-blue); text-align: center;
  }
  .services {
    position: absolute; left: 385px; top: 300px;
    font-family: "Crimson Pro", serif;
    font-weight: 800; font-size: 54px; line-height: 58px;
    color: var(--brand-blue); text-align: center; white-space: nowrap;
    transform: translateX(-50%) scaleX(0.88);
  }
  .chair-photo {
    position: absolute; left: 770px; top: 132px;
    width: 403px; height: 440px;
    border-radius: 12px;
    background: linear-gradient(160deg, var(--chair-blue) 0%, #a9d4ee 50%, var(--chair-grey) 100%);
  }
  .appointment-band {
    position: absolute; left: 0; top: 522px; width: 790px; height: 78px;
  }
  .appointment-band svg { position: absolute; inset: 0; }
  .appointment-text {
    position: absolute; left: 30px; top: 0; height: 78px;
    display: flex; align-items: center;
    font-family: "Crimson Pro", serif;
    font-style: italic; font-weight: 600; font-size: 38px;
    color: var(--white); white-space: nowrap;
    transform: scaleX(0.9); transform-origin: left center;
  }
</style>
</head>
<body>
<main class="canvas">
  <section class="window-cover">
    <div class="top-band"></div>

    <span class="brand-mark"></span>
    <h1 class="brand-name">Pruitt<br>Denatl Laboratory</h1>

    <p class="services">
      DIGITAL CAD &nbsp;|&nbsp; IMPLANTS |<br>
      DENTURES &nbsp;|&nbsp; CAST PARTIALS |<br>
      ORTHODONTIC APPLIANCES
    </p>

    <div class="chair-photo" role="img" aria-label="Photo of a teddy bear sitting in a blue dental chair"></div>

    <div class="appointment-band">
      <svg width="790" height="78" viewBox="0 0 790 78" aria-hidden="true">
        <polygon points="0,0 718,0 788,78 0,78" fill="#0355a3"/>
      </svg>
      <p class="appointment-text">DENTURIST : ON SITE BY APPOINTMENT ONLY</p>
    </div>
  </section>
</main>
</body>
</html>
```